Velmoro Crafts

I would like to have a more comprehensive e-commerce website.

Please use my current website as reference and its content: https://velmorocrafts.com/.

Please code the website. I'd like to have e-commerce functionalities.

```html
<!DOCTYPE html>
<html lang="en">
<head>
<meta charset="utf-8">
<title>Velmoro Crafts — Handcrafted Candles</title>
<link href="https://fonts.googleapis.com/css2?family=Lato:wght@400;700;900&display=swap" rel="stylesheet">
<style>
:root{
  --red:#e8333f;
  --navy:#0f2234;
  --ink:#1b1b1b;
  --muted:#555;
  --hero:#e9e7e8;
  --panel:#e7e7e7;
  --footer:#efefef;
  --star:#f29b1d;
  --line:#dcdcdc;
}
*{box-sizing:border-box;margin:0;padding:0}
html,body{width:1200px;height:5296px;overflow:hidden;background:#fff}
body{font-family:'Lato',sans-serif;color:var(--ink);position:relative}
.abs{position:absolute}
.ph{position:absolute;border-radius:2px}
a{color:inherit;text-decoration:none}

.header{position:absolute;left:0;top:0;width:1200px;height:112px;background:#fff}
.brand{position:absolute;left:118px;top:30px;display:flex;align-items:center;gap:10px;font-weight:900;font-size:15px;letter-spacing:.5px;color:var(--ink)}
.brand .dot{width:34px;height:34px;border-radius:50%;background:var(--red)}
.search{position:absolute;left:372px;top:22px;width:346px;height:34px;background:#d8d8d8;border-radius:4px;font-size:12px;color:#666;padding:9px 20px}
.search svg{position:absolute;right:12px;top:10px}
.nav{position:absolute;left:380px;top:76px;display:flex;gap:40px;font-size:14px;color:#444}
.nav .active{color:var(--red);text-decoration:underline;text-underline-offset:4px}
.tools{position:absolute;left:916px;top:20px;display:flex;gap:10px;align-items:center;font-size:12px;font-weight:700}
.btn{display:inline-block;border-radius:4px;font-size:12px;color:#fff;padding:0 18px;line-height:34px;white-space:nowrap}
.btn.red{background:var(--red)}
.btn.navy{background:var(--navy)}
.btn.sm{font-size:11px;line-height:30px;padding:0 10px;font-weight:700}

.hero{position:absolute;left:0;top:112px;width:1200px;height:506px;background:var(--hero)}
.hero .welcome{position:absolute;left:110px;top:68px;font-size:17px;font-weight:700}
.hero h1{position:absolute;left:110px;top:106px;font-size:56px;line-height:65px;font-weight:700}
.red-t{color:var(--red)}
.hero p{position:absolute;left:110px;top:318px;width:500px;font-size:12px;line-height:24px;color:#444}
.hero .btn{position:absolute;left:110px;top:406px;line-height:42px;font-size:12px}

.title{position:absolute;font-size:40px;font-weight:400}
.title span{color:var(--red);font-weight:700}
.arrows{position:absolute;display:flex;gap:4px}
.arrows i{width:26px;height:26px;border-radius:50%;display:block;position:relative}
.arrows i.l{background:var(--red)}
.arrows i.r{background:#bdbdbd}
.arrows i::after{content:"";position:absolute;top:9px;left:10px;width:7px;height:7px;border-top:2px solid #fff;border-left:2px solid #fff;transform:rotate(-45deg)}
.arrows i.r::after{transform:rotate(135deg);left:7px}

.cat{position:absolute;top:773px;width:318px;height:417px;border-radius:4px;overflow:hidden}
.cat b{position:absolute;bottom:26px;left:0;right:0;text-align:center;color:#fff;font-size:29px;font-weight:700}

.card{position:absolute;width:232px}
.card .img{width:232px;height:282px;border-radius:2px;position:relative}
.card h4{font-size:20px;font-weight:700;margin-top:14px;white-space:nowrap}
.card .price{color:var(--red);font-size:17px;margin-top:2px}
.stars{color:var(--star);font-size:13px;letter-spacing:1px}
.card .btn{position:absolute;right:0;top:304px}
.overlay{position:absolute;right:8px;top:28px;width:36px;height:92px;background:#fff;border-radius:4px;display:flex;flex-direction:column;align-items:center;justify-content:space-around;padding:4px 0}

.about{position:absolute;left:0;top:1833px;width:1200px;height:517px;background:var(--panel)}
.about h2{position:absolute;left:643px;top:76px;font-size:42px;font-weight:400}
.about h2 span{color:var(--red);font-weight:700}
.about h3{position:absolute;left:643px;top:138px;font-size:23px;font-weight:700}
.about p{position:absolute;left:643px;top:180px;width:445px;font-size:11.5px;line-height:31px;color:#444}
.about .btn{position:absolute;left:643px;top:384px;line-height:40px}

.connect{position:absolute;left:111px;top:3573px;width:977px;height:330px;border-radius:10px;overflow:hidden;background:var(--navy)}
.connect h2{position:absolute;left:55px;top:62px;font-size:40px;color:#fff;font-weight:700}
.connect p{position:absolute;left:55px;top:128px;width:420px;font-size:12.5px;line-height:27px;color:#e6e6e6}
.connect .btn{position:absolute;left:45px;top:202px;line-height:40px}

.custom{position:absolute;left:111px;top:4493px;width:977px;height:397px;border-radius:10px;overflow:hidden;background:linear-gradient(90deg,#f7f3ee 0%,#efe7dc 55%,#d9c4a4 100%)}
.custom h2{position:absolute;left:42px;top:46px;font-size:40px;line-height:54px;font-weight:700;color:#222}
.custom .row{position:absolute;left:45px;display:flex;align-items:center;gap:16px;font-size:19px;font-weight:700}
.ic{width:46px;height:46px;border-radius:50%;background:var(--red);display:flex;align-items:center;justify-content:center}
.custom .btn{position:absolute;left:52px;top:312px;line-height:40px}

.footer{position:absolute;left:0;top:4975px;width:1200px;height:321px;background:var(--footer)}
.footer .fbrand{position:absolute;left:110px;top:130px;font-size:19px;font-weight:900;color:var(--ink)}
.footer .fmark{position:absolute;left:180px;top:40px;width:80px;height:80px;border-radius:50%;background:var(--red)}
.social{position:absolute;left:184px;top:166px;display:flex;gap:8px}
.social i{width:18px;height:18px;background:#9aa0aa;display:block;border-radius:2px}
.fcol{position:absolute;font-size:11.5px;color:#444;line-height:27px}
.fcol h5{font-size:16px;font-weight:700;color:#222;margin-bottom:6px}
.frow{display:flex;align-items:center;gap:18px;margin-bottom:22px}
.fic{width:26px;height:26px;border-radius:5px;background:var(--red);display:flex;align-items:center;justify-content:center}
.pay{position:absolute;left:110px;top:266px;display:flex;gap:6px}
.pay i{width:32px;height:20px;border-radius:3px;background:#d5d7dc;display:block}
.copy{position:absolute;left:0;right:0;top:270px;text-align:center;font-size:12px;color:#333}
.fline{position:absolute;left:110px;right:110px;top:252px;border-top:1px solid var(--line)}
</style>
</head>
<body>

<header class="header">
  <div class="brand"><span class="dot"></span>VELMORO CRAFTS</div>
  <div class="search">Search Here...
    <svg width="14" height="14" viewBox="0 0 14 14" fill="none" stroke="#333" stroke-width="1.6"><circle cx="6" cy="6" r="4.5"/><path d="M9.5 9.5L13 13"/></svg>
  </div>
  <nav class="nav"><a class="active">Home</a><a>About Us</a><a>Products</a><a>Contact Us</a></nav>
  <div class="tools">
    <svg width="16" height="16" viewBox="0 0 16 16" fill="none" stroke="#222" stroke-width="1.4"><circle cx="8" cy="5" r="3"/><path d="M2 15c0-3.5 2.7-5.5 6-5.5s6 2 6 5.5"/></svg>
    <svg width="17" height="16" viewBox="0 0 17 16" fill="none" stroke="#222" stroke-width="1.4"><path d="M8.5 14S1.5 9.8 1.5 5.3A3.5 3.5 0 0 1 8.5 4a3.5 3.5 0 0 1 7 1.3C15.5 9.8 8.5 14 8.5 14z"/></svg>
    <svg width="19" height="17" viewBox="0 0 19 17" fill="none" stroke="#222" stroke-width="1.4"><path d="M1 1h3l2 10h10l2-7H5"/><circle cx="7" cy="15" r="1.3"/><circle cx="15" cy="15" r="1.3"/></svg>
    <span style="display:flex;align-items:center;gap:4px;margin-left:20px">
      <svg width="17" height="17" viewBox="0 0 17 17" fill="none" stroke="#222" stroke-width="1.3"><circle cx="8.5" cy="8.5" r="7"/><ellipse cx="8.5" cy="8.5" rx="3" ry="7"/><path d="M1.5 8.5h14"/></svg>ENG ▾</span>
  </div>
  <a class="btn red abs" style="left:918px;top:62px">Explore Our Products</a>
</header>

<section class="hero">
  <div class="welcome">Welcome to Velmoro Crafts!</div>
  <h1>Handcrafted<br><span class="red-t">Candles</span> Inspired<br>by the <span class="red-t">Southwest</span></h1>
  <p>We are a family-owned business passionate about creating beautiful, eco-friendly candles that capture the essence of the Southwest. Our candles are handcrafted by Mexican-American women who pour their love and creativity into each piece.</p>
  <a class="btn navy">Discover Our Handcrafted Candles</a>
  <div class="ph" role="img" aria-label="Three grey textured concrete candles with handmade tags" style="left:630px;top:108px;width:495px;height:340px;background:radial-gradient(ellipse at 50% 55%,#8c8782 0%,#b3ada8 45%,rgba(233,231,232,0) 72%)"></div>
</section>

<h2 class="title" style="left:111px;top:682px">Our <span>Categories</span></h2>
<div class="cat" role="img" aria-label="Round concrete candle topped with colourful wax succulents" style="left:111px;background:linear-gradient(160deg,#7a6f63,#c9c2b8 50%,#3d3935)"><b>Mesa Collection</b></div>
<div class="cat" role="img" aria-label="Fluted white candle holder with a green succulent" style="left:441px;background:linear-gradient(160deg,#6e5a4a,#5f8a4b 45%,#d4d4d0 75%,#3f3b37)"><b>Sierra Collection</b></div>
<div class="cat" role="img" aria-label="Wavy white concrete tray with stones and small plants" style="left:770px;background:linear-gradient(160deg,#4a3a2c,#9b8670 40%,#e2ded8 70%,#2f2a25)"><b>Canyon Collection</b></div>

<h2 class="title" style="left:115px;top:1268px">Mesa <span>Collections</span></h2>
<div class="arrows" style="left:1030px;top:1279px"><i class="l"></i><i class="r"></i></div>

<div class="card" style="left:111px;top:1358px">
  <div class="img" role="img" aria-label="Faceted grey concrete candle" style="background:linear-gradient(160deg,#e9e7e4,#bdb8b2)"></div>
  <h4>Aurelia</h4><div class="price">$34.00</div><div class="stars">★★★★★</div>
  <a class="btn navy sm">Shop Now</a>
</div>
<div class="card" style="left:358px;top:1358px">
  <div class="img" role="img" aria-label="Round textured candle resting on river stones" style="background:linear-gradient(160deg,#8a7f70,#c8c4bf 50%,#6d6356)"></div>
  <h4>Lumen</h4><div class="price">$35.00</div><div class="stars">★★★★★</div>
  <a class="btn navy sm">Shop Now</a>
</div>
<div class="card" style="left:606px;top:1358px">
  <div class="img" role="img" aria-label="Fire bowl candle burning at night" style="background:radial-gradient(ellipse at 45% 40%,#f08a2a 0%,#7a2e0c 35%,#141010 70%)">
    <div class="overlay">
      <svg width="15" height="13" viewBox="0 0 19 17" fill="none" stroke="#444" stroke-width="1.6"><path d="M1 1h3l2 10h10l2-7H5"/><circle cx="7" cy="15" r="1.3"/><circle cx="15" cy="15" r="1.3"/></svg>
      <svg width="14" height="13" viewBox="0 0 17 16" fill="none" stroke="#444" stroke-width="1.6"><path d="M8.5 14S1.5 9.8 1.5 5.3A3.5 3.5 0 0 1 8.5 4a3.5 3.5 0 0 1 7 1.3C15.5 9.8 8.5 14 8.5 14z"/></svg>
      <svg width="15" height="10" viewBox="0 0 16 10" fill="none" stroke="#444" stroke-width="1.4"><path d="M1 5s3-4 7-4 7 4 7 4-3 4-7 4-7-4-7-4z"/><circle cx="8" cy="5" r="2"/></svg>
    </div>
  </div>
  <h4>Ember</h4><div class="price">$7.00</div><div class="stars">★★★★★</div>
  <a class="btn red sm">Add To Cart</a>
</div>
<div class="card" style="left:854px;top:1358px">
  <div class="img" role="img" aria-label="Concrete candle with colourful wax succulents" style="background:linear-gradient(160deg,#d9903a,#6a7fd0 35%,#e8e6e2 60%,#a9a49e)"></div>
  <h4>Blossom</h4><div class="price">$7.00</div><div class="stars">★★★★★</div>
  <a class="btn navy sm">Shop Now</a>
</div>

<section class="about">
  <div class="ph" role="img" aria-label="Two concrete candles with wax succulents and handmade tags" style="left:0;top:4px;width:553px;height:510px;background:linear-gradient(150deg,#3a3633,#8f7fb8 35%,#e3dfd8 60%,#6b5f52)"></div>
  <h2>About <span>Velmoro Crafts</span></h2>
  <h3>Sharing the beauty of the Southwest</h3>
  <p>Velmoro Crafts is a Hispanic woman-owned business that began with a simple dream. Co-founder Marisol Vega, captivated by the art of crafting, started creating candles as gifts for loved ones. Inspired to minimize waste, Marisol envisioned eco-friendly containers that could be repurposed after the candle burned. This passion project took root in her backyard, where she designed and crafted the very first Velmoro candles.</p>
  <a class="btn navy">Read More</a>
</section>

<h2 class="title" style="left:115px;top:2418px">Sierra <span>Collections</span></h2>
<div class="arrows" style="left:1030px;top:2429px"><i class="l"></i><i class="r"></i></div>
<div class="ph" role="img" aria-label="Diamond-textured grey candle" style="left:108px;top:2508px;width:204px;height:338px;background:linear-gradient(160deg,#f2f1ef,#b7b2ad)"></div>
<div class="ph" role="img" aria-label="Fluted white candle with wax spiral on a stone surface" style="left:332px;top:2508px;width:533px;height:332px;background:linear-gradient(160deg,#5f7a45,#9a8f84 40%,#e8e6e3 60%,#5b524a)"></div>
<div class="abs" style="left:755px;top:2514px;width:104px;height:40px;background:var(--red);color:#fff;font-size:19px;line-height:40px;text-align:center">Sale</div>
<div class="abs" style="left:339px;top:2862px;font-size:20px;font-weight:700">Dune Ridge</div>
<div class="abs" style="left:339px;top:2892px;font-size:17px;color:var(--red)">$10.00</div>
<div class="abs stars" style="left:794px;top:2854px">★★★★★</div>
<a class="btn navy sm abs" style="left:766px;top:2884px">Add To Cart</a>
<div class="ph" role="img" aria-label="Faceted white planter with an aloe plant" style="left:882px;top:2508px;width:206px;height:338px;background:linear-gradient(160deg,#f4f4f3,#5f7d4a 40%,#d7d5d1 70%)"></div>

<h2 class="title" style="left:115px;top:3003px">Canyon <span>Collections</span></h2>
<div class="arrows" style="left:1030px;top:3014px"><i class="l"></i><i class="r"></i></div>

<div class="card" style="left:111px;top:3093px">
  <div class="img" role="img" aria-label="Round concrete tray with succulents and stones" style="background:linear-gradient(160deg,#6f8a55,#c9c3b8 55%,#8a8278)"></div>
  <h4>Oasis</h4><div class="price">$35.00</div><div class="stars">★★★★★</div>
  <a class="btn navy sm">Shop Now</a>
</div>
<div class="card" style="left:358px;top:3093px">
  <div class="img" role="img" aria-label="Oval candle tray with small wax figures" style="background:linear-gradient(160deg,#6b7fa8,#d8d3c8 55%,#9fa6b4)"></div>
  <h4>Lumen</h4><div class="price">$7.00</div><div class="stars">★★★★★</div>
  <a class="btn navy sm">Shop Now</a>
</div>
<div class="card" style="left:606px;top:3093px">
  <div class="img" role="img" aria-label="Concrete bowl candle with wax pumpkins" style="background:linear-gradient(160deg,#e08a2c,#f0ece5 45%,#b6b0a8)">
    <div class="overlay">
      <svg width="15" height="13" viewBox="0 0 19 17" fill="none" stroke="#444" stroke-width="1.6"><path d="M1 1h3l2 10h10l2-7H5"/><circle cx="7" cy="15" r="1.3"/><circle cx="15" cy="15" r="1.3"/></svg>
      <svg width="14" height="13" viewBox="0 0 17 16" fill="none" stroke="#444" stroke-width="1.6"><path d="M8.5 14S1.5 9.8 1.5 5.3A3.5 3.5 0 0 1 8.5 4a3.5 3.5 0 0 1 7 1.3C15.5 9.8 8.5 14 8.5 14z"/></svg>
      <svg width="15" height="10" viewBox="0 0 16 10" fill="none" stroke="#444" stroke-width="1.4"><path d="M1 5s3-4 7-4 7 4 7 4-3 4-7 4-7-4-7-4z"/><circle cx="8" cy="5" r="2"/></svg>
    </div>
  </div>
  <h4>Harvest Pumpkin</h4><div class="price">$35.00</div><div class="stars">★★★★★</div>
  <a class="btn red sm" style="top:330px">Add To Cart</a>
</div>
<div class="card" style="left:854px;top:3093px">
  <div class="img" role="img" aria-label="Heart-shaped concrete candle" style="background:linear-gradient(160deg,#f3f2f0,#9c9892 55%,#e4e2df)"></div>
  <h4>Amora</h4><div class="price">$35.00</div><div class="stars">★★★★★</div>
  <a class="btn navy sm">Shop Now</a>
</div>

<section class="connect">
  <svg class="abs" style="left:0;top:0" width="977" height="330" viewBox="0 0 977 330"><path d="M600 0H977V330H560C520 240 520 90 600 0Z" fill="#e0303c"/></svg>
  <div class="ph" role="img" aria-label="Concrete bowl candle with a handmade tag" style="left:600px;top:40px;width:300px;height:250px;background:radial-gradient(ellipse at 50% 45%,#f4f2ee 0%,#9a948e 45%,rgba(224,48,60,0) 72%)"></div>
  <h2>Let's Connect!</h2>
  <p>We would love to hear from you! Have questions about our candles or want to learn more about Velmoro Crafts?</p>
  <a class="btn red">Discover Our Handcrafted Candles</a>
</section>

<h2 class="title" style="left:110px;top:3978px">New <span>Collections</span></h2>
<div class="arrows" style="left:1030px;top:3989px"><i class="l"></i><i class="r"></i></div>
<div class="ph" role="img" aria-label="Latte-style candle in a glass cup" style="left:111px;top:4068px;width:204px;height:337px;background:linear-gradient(180deg,#f1efec,#c9a78a 55%,#6e4a35 75%,#e4e1dd)"></div>
<div class="ph" role="img" aria-label="Candle topped with wax cereal rings in a glass mug" style="left:328px;top:4068px;width:264px;height:337px;background:linear-gradient(180deg,#f1efec,#d9a07a 45%,#f3f1ee 75%,#dcd9d5)"></div>
<div class="ph" role="img" aria-label="Layered coffee candle in a tall glass" style="left:610px;top:4068px;width:263px;height:337px;background:linear-gradient(180deg,#f2f0ed,#8a5b3e 50%,#d7d3cf)"></div>
<div class="ph" role="img" aria-label="Candle bowl with pastel wax macarons" style="left:884px;top:4068px;width:206px;height:337px;background:linear-gradient(180deg,#e9e8e6,#a9c3d9 45%,#e7b6c7 60%,#f4f3f1)"></div>

<section class="custom" role="img" aria-label="Lit white candles with dried pampas grass">
  <div class="ph" style="left:600px;top:0;width:377px;height:397px;background:radial-gradient(circle at 65% 30%,#fbf8f2 0%,#e9d8bd 35%,rgba(217,196,164,0) 70%)"></div>
  <h2>Have questions or want to<br>place a <span class="red-t">custom order?</span></h2>
  <div class="row" style="top:176px"><span class="ic"><svg width="22" height="16" viewBox="0 0 22 16" fill="none" stroke="#fff" stroke-width="1.8"><rect x="1" y="1" width="20" height="14" rx="1.5"/><path d="M1 2l10 7 10-7"/></svg></span>hello@velmorocrafts.com</div>
  <div class="row" style="top:240px"><span class="ic"><svg width="20" height="20" viewBox="0 0 24 24" fill="#fff"><path d="M6.6 10.8a15.1 15.1 0 0 0 6.6 6.6l2.2-2.2a1 1 0 0 1 1-.25 11.4 11.4 0 0 0 3.6.57 1 1 0 0 1 1 1V20a1 1 0 0 1-1 1A17 17 0 0 1 3 4a1 1 0 0 1 1-1h3.5a1 1 0 0 1 1 1c0 1.25.2 2.45.57 3.57a1 1 0 0 1-.25 1z"/></svg></span>+1 888 888 8888</div>
  <a class="btn navy">Contact Us</a>
</section>

<footer class="footer">
  <div class="fmark"></div>
  <div class="fbrand">VELMORO CRAFTS</div>
  <div class="social"><i></i><i></i></div>
  <div class="fcol" style="left:458px;top:50px"><h5>Quick Links</h5>Home<br>About Us<br>Products<br>Contact Us</div>
  <div class="fcol" style="left:625px;top:46px"><h5>Help Links</h5>Support Center<br>Delivery &amp; Returns<br>Terms &amp; Conditions<br>Products Return<br>Wholesale Policy</div>
  <div class="fcol" style="left:875px;top:40px;width:220px"><h5 style="margin-bottom:14px">Contact Info</h5>
    <div class="frow"><span class="fic"><svg width="12" height="14" viewBox="0 0 12 16" fill="#fff"><path d="M6 0a6 6 0 0 0-6 6c0 4.5 6 10 6 10s6-5.5 6-10a6 6 0 0 0-6-6zm0 8.5A2.5 2.5 0 1 1 6 3.5a2.5 2.5 0 0 1 0 5z"/></svg></span>Lorem Ipsum ,USA -437916</div>
    <div class="frow"><span class="fic"><svg width="13" height="13" viewBox="0 0 24 24" fill="#fff"><path d="M6.6 10.8a15.1 15.1 0 0 0 6.6 6.6l2.2-2.2a1 1 0 0 1 1-.25 11.4 11.4 0 0 0 3.6.57 1 1 0 0 1 1 1V20a1 1 0 0 1-1 1A17 17 0 0 1 3 4a1 1 0 0 1 1-1h3.5a1 1 0 0 1 1 1c0 1.25.2 2.45.57 3.57a1 1 0 0 1-.25 1z"/></svg></span>+1 888 888 88888</div>
    <div class="frow"><span class="fic"><svg width="14" height="10" viewBox="0 0 22 16" fill="none" stroke="#fff" stroke-width="2"><rect x="1" y="1" width="20" height="14"/><path d="M1 2l10 7 10-7"/></svg></span>hello@velmorocrafts.com</div>
  </div>
  <div class="fline"></div>
  <div class="pay"><i></i><i></i><i></i><i></i><i></i><i></i></div>
  <div class="copy">© 2025 Velmoro Craft.All Rights Reserved</div>
</footer>

</body>
</html>
```